Business Card design for new private practice opening

I need a business card design for my new private practice with my new logo uploaded as a file
On the front the logo
On the back: maybe a small logo somewhere?
Priv. Doz. DDr. Corinna Vestaluk
Fachärztin für Allgemein- & Viszeralchirurgie
Address: xxx
Tel: xxx
Mobil:xxx
Webseite:xxx
Email:xxx

Contact Information for Business Card

See project description above for details

Requirements
Nice to have
• I would like the colors of the logo incorporated into the business card

```html
<!DOCTYPE html>
<html lang="de">
<head>
<meta charset="utf-8">
<title>Vestaluk Chirurgie – Visitenkarte</title>
<link href="https://fonts.googleapis.com/css2?family=Montserrat:wght@400;600;700&display=swap" rel="stylesheet">
<style>
  :root {
    --bg: #e9eef0;
    --paper: #f7f7f5;
    --teal: #35b5ad;
    --grey: #7a7a7a;
    --white: #ffffff;
  }
  * { box-sizing: border-box; margin: 0; padding: 0; }
  html, body { width: 1200px; height: 1038px; overflow: hidden; }
  body {
    background: var(--bg);
    font-family: "Montserrat", sans-serif;
    display: flex;
    flex-direction: column;
    align-items: center;
    justify-content: center;
    gap: 64px;
  }
  .card {
    width: 600px;
    height: 345px;
    position: relative;
    box-shadow: 0 6px 18px rgba(0,0,0,.12);
    overflow: hidden;
  }

  /* Front */
  .card-front {
    background: var(--paper);
    display: flex;
    align-items: center;
    justify-content: center;
    gap: 22px;
  }
  .brand-mark {
    border-radius: 50%;
    flex: none;
  }
  .card-front .brand-mark {
    width: 86px; height: 86px;
    border: 4px solid var(--grey);
  }
  .brand-name {
    font-weight: 700;
    text-transform: uppercase;
    line-height: 1.02;
    letter-spacing: .5px;
  }
  .card-front .brand-name { color: var(--grey); font-size: 38px; }

  /* Back */
  .card-back { background: var(--teal); color: var(--white); }
  .back-brand {
    position: absolute;
    top: 40px; right: 44px;
    display: flex; align-items: center; gap: 12px;
  }
  .card-back .brand-mark {
    width: 50px; height: 50px;
    border: 3px solid var(--white);
  }
  .card-back .brand-name { font-size: 21px; color: var(--white); }

  .contact-list {
    position: absolute;
    top: 122px; right: 44px;
    list-style: none;
  }
  .contact-list::after {
    content: "";
    position: absolute;
    right: 10px; top: 10px; bottom: 10px;
    width: 2px; background: var(--white);
  }
  .contact-item {
    display: flex; align-items: center; justify-content: flex-end;
    gap: 10px;
    height: 30px;
    font-size: 14px;
    letter-spacing: .3px;
  }
  .contact-icon {
    width: 22px; height: 22px;
    border-radius: 50%;
    background: var(--white);
    display: flex; align-items: center; justify-content: center;
    position: relative; z-index: 1;
  }
  .contact-icon svg { width: 13px; height: 13px; }

  .person {
    position: absolute;
    left: 40px; bottom: 82px;
  }
  .person-name { font-size: 11px; font-weight: 400; letter-spacing: .3px; }
  .person-name strong { font-size: 20px; font-weight: 700; letter-spacing: 0; }
  .person-title { font-size: 9px; margin-top: 4px; letter-spacing: .2px; }

  .address-band {
    position: absolute;
    left: 0; right: 0; bottom: 0;
    height: 50px;
    background: var(--paper);
    color: var(--grey);
    font-size: 15px;
    display: flex; align-items: center; justify-content: center;
    letter-spacing: .3px;
  }
</style>
</head>
<body>

  <section class="card card-front" aria-label="Vorderseite">
    <span class="brand-mark" aria-hidden="true"></span>
    <h1 class="brand-name">Vestaluk<br>Chirurgie</h1>
  </section>

  <section class="card card-back" aria-label="Rückseite">
    <div class="back-brand">
      <span class="brand-mark" aria-hidden="true"></span>
      <p class="brand-name">Vestaluk<br>Chirurgie</p>
    </div>

    <ul class="contact-list">
      <li class="contact-item">555-318-2046
        <span class="contact-icon"><svg viewBox="0 0 12 12"><rect x="3" y="0.5" width="6" height="11" rx="1.2" fill="none" stroke="#35b5ad" stroke-width="1.3"/><circle cx="6" cy="9.3" r=".7" fill="#35b5ad"/></svg></span>
      </li>
      <li class="contact-item">555-318-2047
        <span class="contact-icon"><svg viewBox="0 0 12 12"><path d="M2.5 1l2 .3.8 2.4-1.2 1a6 6 0 0 0 3.2 3.2l1-1.2 2.4.8.3 2c-.2.8-1 1.2-1.8 1A10 10 0 0 1 1.5 2.8C1.3 2 1.7 1.2 2.5 1z" fill="#35b5ad"/></svg></span>
      </li>
      <li class="contact-item">praxis@vestaluk.example
        <span class="contact-icon"><svg viewBox="0 0 12 12"><rect x="1" y="2.5" width="10" height="7" rx=".8" fill="none" stroke="#35b5ad" stroke-width="1.2"/><path d="M1.3 3l4.7 3.6L10.7 3" fill="none" stroke="#35b5ad" stroke-width="1.2"/></svg></span>
      </li>
      <li class="contact-item">www.vestaluk.example
        <span class="contact-icon"><svg viewBox="0 0 12 12"><circle cx="6" cy="6" r="4.8" fill="none" stroke="#35b5ad" stroke-width="1.1"/><ellipse cx="6" cy="6" rx="2" ry="4.8" fill="none" stroke="#35b5ad" stroke-width="1"/><path d="M1.2 6h9.6" stroke="#35b5ad" stroke-width="1"/></svg></span>
      </li>
    </ul>

    <div class="person">
      <p class="person-name">Priv. Doz. DDr. <strong>Corinna Vestaluk</strong></p>
      <p class="person-title">Fachärztin für Allgemein- &amp; Viszeralchirurgie</p>
    </div>

    <p class="address-band">4870 Linden Park Ave Suite 2 Dayton, Ohio ###</p>
  </section>

</body>
</html>
```